Ice Cream Cup Design

We need a packaging design for ice cream cups.
We're a London based company called Villa Rosa Dolci and are producers of fresh Italian Artisan Gelato our website is www.villarosadolci.co.uk

We're looking to invest in a cup filling machine to fill 100ml and 500ml cups of gelato.
The 500ml cup will be the same shape and height as the Nordvik Freeze tub with a matching lid design.
The 100ml cup will be of the same shape and height of the Nordvik Freeze Single Serve cup with a matching lid design and includes a spoon inside.

We're looking for edgy clean designs that give an impression of quality and draw attention to the product if it sat on a product shelf. Inspired by packaging such as Ko, Pemberly and Harrowfield we're keen on a black themed packaging with a striking contrast of simple colour and a simple ice cream or gelato image that shows more than one flavour.
This particular design is not boasting any particular flavour, its a uniform design across our whole range of flavours.

Our company logo may be too fussy for this packaging so we would like to include our company ice cream logo and a way to include our company name but still look edgy for example - just like Pemberly Tea - our ice cream logo big G underneath, then 'VILLA ROSA DOLCI' underneath, and below that 'ARTISAN ITALIAN GELATO'. Or anything that inspires and looks good, will draw attention and looks sexy and indulgent and gives an impression of luxury product.

Please check attached document for cup shape and dimensions.

Reason: Christmas and New Year Holiday period resulted in less time for feedback opportunity and new designs to be posted.

Target Market(s)

Target market between 20-40 years old, consumers of quality desserts all year round.

Industry/Entity Type

It Company

Requirements
Must have
• Our Ice Cream Logo
Our name (doesn't need to necessarily have it in our font, can be in bold lettering)
Nice to have
• Limited writing and fuss.
Ideal to have simple clean designs
Should not have
• Eccentric colours and fun childlike images.

```html
<!DOCTYPE html>
<html lang="en">
<head>
<meta charset="utf-8">
<title>Villa Rosa Dolci – Gelato Cup Dieline</title>
<link rel="stylesheet" href="https://fonts.googleapis.com/css2?family=Parisienne&family=Cormorant+Garamond:wght@500&family=Marcellus&display=swap">
<style>
  :root {
    --paper: #ffffff;
    --ink: #000000;
    --chrome-light: #f4f4f4;
    --chrome-mid: #9a9a9a;
    --chrome-dark: #2a2a2a;
    --teal: #5f9c9b;
    --teal-light: #8fc0bd;
    --gold: #cdb66b;
  }
  html, body {
    margin: 0;
    padding: 0;
    width: 1200px;
    height: 874px;
    overflow: hidden;
    background: var(--paper);
  }
  .dieline {
    position: relative;
    width: 1200px;
    height: 874px;
  }
  .dieline svg {
    position: absolute;
    inset: 0;
  }
  .lid-name {
    font-family: "Parisienne", cursive;
    font-size: 34px;
    fill: var(--teal);
  }
  .wrap-name {
    font-family: "Parisienne", cursive;
    font-size: 36px;
    fill: var(--teal);
  }
  .wrap-tagline {
    font-family: "Cormorant Garamond", serif;
    font-weight: 500;
    font-size: 15px;
    fill: var(--teal-light);
  }
  .wrap-artisan {
    font-family: "Marcellus", serif;
    font-size: 15px;
    letter-spacing: 0.5px;
    fill: var(--teal-light);
  }
  .wrap-gelato {
    font-family: "Parisienne", cursive;
    font-size: 28px;
    fill: var(--gold);
  }
  .brand-dot {
    fill: none;
    stroke: var(--teal);
    stroke-width: 2;
  }
</style>
</head>
<body>
<main class="dieline">
  <svg width="1200" height="874" viewBox="0 0 1200 874" xmlns="http://www.w3.org/2000/svg">
    <defs>
      <linearGradient id="lid-rim" x1="0" y1="0" x2="1" y2="1">
        <stop offset="0" stop-color="var(--chrome-dark)"/>
        <stop offset="0.3" stop-color="var(--chrome-light)"/>
        <stop offset="0.55" stop-color="var(--chrome-mid)"/>
        <stop offset="0.8" stop-color="var(--chrome-light)"/>
        <stop offset="1" stop-color="var(--chrome-dark)"/>
      </linearGradient>
      <linearGradient id="wrap-sheen" x1="0" y1="0" x2="1" y2="0">
        <stop offset="0" stop-color="#3b3b3b"/>
        <stop offset="0.2" stop-color="#d9d9d9"/>
        <stop offset="0.36" stop-color="#141414"/>
        <stop offset="0.64" stop-color="#141414"/>
        <stop offset="0.8" stop-color="#d9d9d9"/>
        <stop offset="1" stop-color="#3b3b3b"/>
      </linearGradient>
      <linearGradient id="wrap-topline" x1="0" y1="0" x2="1" y2="0">
        <stop offset="0" stop-color="#555"/>
        <stop offset="0.5" stop-color="#ffffff"/>
        <stop offset="1" stop-color="#555"/>
      </linearGradient>
    </defs>

    <!-- Lid -->
    <g class="lid">
      <circle cx="596" cy="220" r="217" fill="url(#lid-rim)"/>
      <circle cx="596" cy="222" r="200" fill="var(--ink)"/>
      <circle class="brand-dot" cx="596" cy="188" r="12"/>
      <text class="lid-name" x="596" y="240" text-anchor="middle">Villa Rosa Dolci</text>
    </g>

    <!-- Cup wrap -->
    <g class="cup-wrap">
      <path d="M57 489 Q596 393 1143 489 L1009 817 Q596 747 189 817 Z" fill="url(#wrap-sheen)"/>
      <path d="M57 489 Q596 393 1143 489 L1138 500 Q596 406 62 500 Z" fill="url(#wrap-topline)" opacity="0.7"/>
      <path class="wrap-body"
            d="M150 590 C230 580 280 510 360 505 C450 500 500 470 596 466 C692 470 742 500 832 505 C912 510 962 580 1050 590
               L1035 700 C950 700 910 650 840 655 C750 660 700 770 596 765 C492 770 442 660 352 655 C282 650 242 700 165 700 Z"
            fill="var(--ink)"/>
      <circle cx="596" cy="640" r="135" fill="var(--ink)"/>

      <circle class="brand-dot" cx="596" cy="565" r="14"/>
      <text class="wrap-name" x="596" y="636" text-anchor="middle">Villa Rosa Dolci</text>
      <text class="wrap-tagline" x="596" y="665" text-anchor="middle">The House of Italian Ice Cream</text>
      <text class="wrap-artisan" x="596" y="691" text-anchor="middle">ARTISAN ITALIAN</text>
      <text class="wrap-gelato" x="596" y="730" text-anchor="middle">Gelato</text>
    </g>
  </svg>
</main>
</body>
</html>
```